Restwell Path App - Featured Graphics/Screenshots and Icon

We need graphics for a new app that is a step-by-step program for treating insomnia.
What is needed:
1) app icon (1024x1024 so it can be scaled down)
2) general featured image for use in advertising and app stores
3) screenshots incorporating text (Based on Cognitive Behavioral Therapy for Insomnia, An Innovative and Interactive Self-Help Program, Recommendations Tailored to Your Sleep Patterns, Track Your Sleep).
We have included a variety of example screenshots from the app.
Example text to include with screenshots and/or feature graphics.
1. Based on Cognitive Behavioral Therapy for Insomnia (CBT-I)
2. CBT-I is recommended as a wise choice by buyer digest and a first-line treatment approach by the Federal Bureau of Wellness (FBW)
3. An Innovative and Interactive Self-Help Program
4. Recommendations Tailored to Your Sleep Patterns
5. Track Your Sleep
Here is an overview of the program:
The Restwell Path is an app developed to enable more access to cognitive-behavior therapy for insomnia (CBT-I). CBT-I is recognized as a first line treatment approach by the Federal Bureau of Wellness, however there are few trained providers of the treatment. The Restwell Path will guide you through the cognitive-behavioral treatment process in a step-by-step manner. You will be introduced to new steps on a weekly basis. The first step is to establish a baseline using sleep logs. This is very important as the information gathered will be used to set your initial sleep/wake schedule. Following this initial step, you will be guided through a process of re-establishing a natural drive to sleep, resetting your circadian rhythm, learning to recognize/manage anxiety, apply productive ways to think about sleep, and ways to prevent relapse. The treatment approach can be challenging. It will require completion of all tasks and maintaining the recommended sleep schedule.
We prefer layered PSD files to allow for easy scaling and / or alteration.
Target Market(s)
Mobile app users with insomnia.
Look and feel

```html
<!DOCTYPE html>
<html lang="en">
<head>
<meta charset="utf-8">
<title>Restwell Path – Welcome</title>
<link rel="stylesheet" href="https://fonts.googleapis.com/css2?family=Poppins:wght@400;500;600&display=swap">
<style>
  :root {
    --sky: #4fb3dc;
    --white: #ffffff;
    --button-text: #4fb3dc;
  }
  * { margin: 0; padding: 0; box-sizing: border-box; }
  html, body {
    width: 677px;
    height: 1200px;
    overflow: hidden;
    background: var(--sky);
  }
  .screen {
    position: relative;
    width: 677px;
    height: 1200px;
    background: var(--sky);
    color: var(--white);
    font-family: "Poppins", sans-serif;
  }
  .status-bar {
    position: absolute;
    top: 0; left: 0; right: 0;
    height: 46px;
    display: flex;
    align-items: center;
    justify-content: space-between;
    padding: 0 14px;
    font-size: 25px;
    font-weight: 400;
  }
  .status-bar .left, .status-bar .right {
    display: flex;
    align-items: center;
    gap: 8px;
  }
  .signal-dots { display: flex; gap: 4px; }
  .signal-dots span {
    width: 11px; height: 11px;
    border-radius: 50%;
    background: var(--white);
  }
  .signal-dots span.empty {
    background: transparent;
    border: 1.5px solid var(--white);
  }
  .brand {
    position: absolute;
    top: 120px;
    left: 0; right: 0;
    display: flex;
    flex-direction: column;
    align-items: center;
  }
  .brand-mark {
    width: 190px; height: 190px;
    border-radius: 50%;
    background: var(--white);
    margin-bottom: 50px;
  }
  .brand-name {
    font-size: 84px;
    font-weight: 500;
    line-height: 1.1;
    text-align: center;
    color: var(--white);
  }
  .actions {
    position: absolute;
    top: 704px;
    left: 185px;
    width: 307px;
    display: flex;
    flex-direction: column;
    gap: 36px;
  }
  .button {
    display: flex;
    align-items: center;
    justify-content: center;
    height: 104px;
    border-radius: 52px;
    font-family: "Poppins", sans-serif;
    font-size: 33px;
    font-weight: 400;
    letter-spacing: 1px;
    text-decoration: none;
  }
  .button-login {
    background: var(--white);
    color: var(--button-text);
  }
  .button-signup {
    border: 4px solid var(--white);
    color: var(--white);
  }
</style>
</head>
<body>
<main class="screen">
  <header class="status-bar">
    <div class="left">
      <div class="signal-dots"><span></span><span></span><span></span><span></span><span class="empty"></span></div>
      <span class="carrier">CREST</span>
      <svg class="wifi" width="28" height="22" viewBox="0 0 28 22" aria-hidden="true">
        <path d="M14 20 L2 7 A17 17 0 0 1 26 7 Z" fill="#ffffff"/>
      </svg>
    </div>
    <div class="right">
      <svg class="bluetooth" width="14" height="24" viewBox="0 0 14 24" aria-hidden="true">
        <path d="M2 6 L12 17 L7 22 V2 L12 7 L2 18" fill="none" stroke="#ffffff" stroke-width="2"/>
      </svg>
      <span class="battery-level">82%</span>
      <svg class="battery" width="56" height="24" viewBox="0 0 56 24" aria-hidden="true">
        <rect x="1" y="2" width="46" height="20" rx="3" fill="none" stroke="#ffffff" stroke-width="2"/>
        <rect x="4" y="5" width="34" height="14" rx="1" fill="#ffffff"/>
        <rect x="48.5" y="8" width="3" height="8" rx="1" fill="#ffffff"/>
      </svg>
      <svg class="charging" width="12" height="24" viewBox="0 0 12 24" aria-hidden="true">
        <path d="M8 1 L1 14 H6 L4 23 L11 10 H6 Z" fill="#ffffff"/>
      </svg>
    </div>
  </header>

  <section class="brand">
    <div class="brand-mark"></div>
    <h1 class="brand-name">Restwell<br>Path</h1>
  </section>

  <nav class="actions">
    <a class="button button-login" href="#">LOG IN</a>
    <a class="button button-signup" href="#">SIGN UP</a>
  </nav>
</main>
</body>
</html>
```